Postcard For neighbors near worksite

We are a residential interior and exterior painting company. I will be sending post cards out in neighborhoods that we will be currently working in. Basically giving the neighbors a "Neighborhood Notice" that we are in the area and would like to give a Free Estimate to anyone in that neighborhood. I will attach a file of another companies idea that I like. Also, I attached my Logo. Brightcoat Painting & More

Target Market(s)

Neighbors near where we are working

Industry/Entity Type

It Company

Requirements
Must have
• Website: Brightcoatpaint.example
• Number: 555.204.6617

```html
<!DOCTYPE html>
<html lang="en">
<head>
<meta charset="utf-8">
<title>Brightcoat Painting &amp; More — Neighbors Notice Postcard</title>
<link rel="stylesheet" href="https://fonts.googleapis.com/css2?family=Anton&family=Open+Sans:wght@400;600;700&family=Roboto+Condensed:wght@700&display=swap">
<style>
  :root {
    --bg: #eeeae4;
    --charcoal-dark: #232323;
    --charcoal-light: #5a5a5a;
    --brand-red: #e41b17;
    --white: #ffffff;
    --ink-light: #e8e8e8;
    --photo-blue: #1f6fe0;
    --photo-pale: #eef0f2;
    --rule: #6d6d6d;
  }
  * { box-sizing: border-box; margin: 0; padding: 0; }
  html, body { width: 1020px; height: 1200px; overflow: hidden; background: var(--bg); }
  .sheet { position: relative; width: 1020px; height: 1200px; }

  .postcard {
    position: absolute; left: 78px; width: 864px; height: 470px;
    overflow: hidden; background: var(--white);
    box-shadow: 0 3px 10px rgba(0,0,0,.25);
  }
  .postcard--front { top: 110px; }
  .postcard--back { top: 624px; }

  .panel-shape { position: absolute; inset: 0; width: 864px; height: 470px; }

  .photo-area {
    position: absolute; top: 0; right: 0; width: 500px; height: 470px;
    background: linear-gradient(100deg, var(--photo-blue) 0%, #5b95e6 22%, var(--photo-pale) 48%, #f6f6f6 70%, #cfd8e6 100%);
  }

  .brand {
    position: absolute; left: 58px; top: 34px;
    display: flex; align-items: center; gap: 10px;
    font-family: "Open Sans", sans-serif; font-weight: 700;
    font-size: 19px; color: var(--white); line-height: 1;
  }
  .brand-mark { width: 16px; height: 16px; background: var(--brand-red); }

  .headline-top {
    position: absolute; left: 56px; top: 122px;
    font-family: "Open Sans", sans-serif; font-weight: 400;
    font-size: 37px; color: var(--white); letter-spacing: .5px; line-height: 1;
  }
  .headline-main {
    position: absolute; left: 54px; top: 160px;
    font-family: "Anton", sans-serif; font-size: 76px;
    color: var(--brand-red); line-height: 1; letter-spacing: 1px;
  }

  .body-copy {
    position: absolute; font-family: "Open Sans", sans-serif;
    font-size: 9.6px; line-height: 1.45; color: var(--ink-light);
  }
  .postcard--front .body-copy { left: 54px; top: 250px; width: 370px; }
  .postcard--back .body-copy { left: 36px; top: 194px; width: 318px; text-align: justify; }

  .section-tag {
    position: absolute; left: 0; top: 128px; width: 212px; height: 50px;
    background: var(--brand-red); color: var(--white);
    font-family: "Roboto Condensed", sans-serif; font-weight: 700;
    font-size: 22px; line-height: 50px; padding-left: 44px;
  }

  .call-block { position: absolute; width: 250px; height: 92px; }
  .postcard--front .call-block { left: 54px; top: 346px; }
  .postcard--back .call-block { left: 36px; top: 354px; }
  .call-splat { position: absolute; inset: 0; width: 250px; height: 92px; }
  .call-text {
    position: absolute; left: 52px; top: 12px; color: var(--white);
    font-family: "Roboto Condensed", sans-serif; font-weight: 700; line-height: 1.1;
  }
  .call-label { font-size: 19px; }
  .call-phone { font-size: 23px; }
  .call-web { font-size: 12px; display: flex; align-items: center; gap: 4px; margin-top: 2px; }
  .call-web-dot { width: 7px; height: 7px; border-radius: 50%; background: var(--white); }

  .stamp-box {
    position: absolute; left: 710px; top: 36px; width: 125px; height: 118px;
    border: 1px solid var(--rule);
  }
  .address-line { position: absolute; left: 550px; width: 286px; height: 1px; background: var(--rule); }
</style>
</head>
<body>
<div class="sheet">

  <section class="postcard postcard--front">
    <div class="photo-area" role="img" aria-label="Photo of a smiling painter in a blue cap rolling blue paint onto a white wall"></div>
    <svg class="panel-shape" viewBox="0 0 864 470" aria-hidden="true">
      <defs>
        <radialGradient id="frontShade" cx="0.45" cy="0.45" r="0.75">
          <stop offset="0" stop-color="#5a5a5a"/>
          <stop offset="1" stop-color="#232323"/>
        </radialGradient>
      </defs>
      <path fill="url(#frontShade)" d="M0 0 L440 0 L418 18 L436 34 L405 52 L430 72 L398 92 L425 114 L392 136 L418 158 L388 182 L414 204 L384 226 L410 248 L380 270 L406 292 L376 316 L402 338 L374 360 L398 384 L370 406 L396 428 L372 450 L392 470 L0 470 Z"/>
    </svg>
    <div class="brand"><span class="brand-mark"></span>Brightcoat Painting &amp; More</div>
    <h1 class="headline-top">NEIGHBORS</h1>
    <h2 class="headline-main">NOTICE</h2>
    <p class="body-copy">Lorem Ipsum is simply dummy text of the printing and typesetting industry. Lorem Ipsum has been the industry's standard dummy text ever since the 1500s, when an unknown printer took a galley of type and scrambled it to make a type specimen book.</p>
    <div class="call-block">
      <svg class="call-splat" viewBox="0 0 250 92" aria-hidden="true">
        <path fill="var(--brand-red)" d="M14 22 L40 10 L70 14 L96 4 L130 12 L160 6 L196 14 L228 10 L240 26 L232 40 L246 54 L234 70 L240 84 L206 80 L176 90 L140 82 L104 90 L70 82 L40 88 L22 76 L8 80 L14 62 L2 48 L12 36 Z"/>
      </svg>
      <div class="call-text">
        <div class="call-label">Call Now</div>
        <div class="call-phone">555.204.6617</div>
        <div class="call-web"><span class="call-web-dot"></span>Brightcoatpaint.example</div>
      </div>
    </div>
  </section>

  <section class="postcard postcard--back">
    <svg class="panel-shape" viewBox="0 0 864 470" aria-hidden="true">
      <defs>
        <radialGradient id="backShade" cx="0.45" cy="0.35" r="0.75">
          <stop offset="0" stop-color="#5a5a5a"/>
          <stop offset="1" stop-color="#232323"/>
        </radialGradient>
      </defs>
      <path fill="url(#backShade)" d="M0 0 L456 0 L434 18 L452 36 L420 56 L446 78 L414 100 L440 122 L408 146 L434 168 L402 192 L428 214 L398 238 L424 260 L394 284 L420 306 L390 330 L416 352 L388 376 L412 398 L384 420 L408 444 L386 470 L0 470 Z"/>
    </svg>
    <div class="brand"><span class="brand-mark"></span>Brightcoat Painting &amp; More</div>
    <div class="section-tag">Lorem Ipsum</div>
    <p class="body-copy">Lorem Ipsum is simply dummy text of the printing and typesetting industry. Lorem Ipsum has been the industry's standard dummy text ever since the 1500s, when an unknown printer took a galley of type and scrambled it to make a type specimen book. It has survived not only five centuries, but also the leap into electronic typesetting, remaining essentially unchanged. It was popularised in the 1960s with the release of Letraset sheets containing Lorem Ipsum passages, and more recently with desktop publishing software like Aldus PageMaker including versions of Lorem Ipsum.</p>
    <div class="call-block">
      <svg class="call-splat" viewBox="0 0 250 92" aria-hidden="true">
        <path fill="var(--brand-red)" d="M14 22 L40 10 L70 14 L96 4 L130 12 L160 6 L196 14 L228 10 L240 26 L232 40 L246 54 L234 70 L240 84 L206 80 L176 90 L140 82 L104 90 L70 82 L40 88 L22 76 L8 80 L14 62 L2 48 L12 36 Z"/>
      </svg>
      <div class="call-text">
        <div class="call-label">Call Now</div>
        <div class="call-phone">555.204.6617</div>
        <div class="call-web"><span class="call-web-dot"></span>Brightcoatpaint.example</div>
      </div>
    </div>
    <div class="stamp-box"></div>
    <div class="address-line" style="top:242px"></div>
    <div class="address-line" style="top:296px"></div>
    <div class="address-line" style="top:348px"></div>
  </section>

</div>
</body>
</html>
```